Lanternfield Prose Studio (LPStudio.net)

We need a Wordpress-based site designed for a client who provides writing and editing services for the IT industry. We have a wireframe complete for the homepage, but need all internal pages designed (based on homepage wireframe) and the entire site coded for WP.

Internal pages include: "Our Work" (with samples & testimonials); "Capabilities" (with sections to address "strategy", "coaching", "writing" and "editing"); "About Us"; and a Contact page.

Will provide all copywriting, writing samples, testimonials, and client logos.

We completely realize/acknowledge the subject matter is visually BORING! Anything at all that can be done to make it look visually appealing would be *great*! Stock photography is fine.

Please feel free to ask any questions whatsoever. Thanks for your time!

```html
<!DOCTYPE html>
<html lang="en">
<head>
<meta charset="utf-8">
<title>Lanternfield Prose Studio</title>
<link rel="stylesheet" href="https://fonts.googleapis.com/css2?family=Montserrat:wght@400;500;600;700;800&family=Open+Sans:wght@400;600&display=swap">
<style>
:root{
  --orange:#f26a21;
  --orange-deep:#e4561a;
  --ink:#1e1e1e;
  --text:#555;
  --muted:#8a8a8a;
  --line:#e4e4e4;
  --band:#ececec;
  --white:#fff;
}
*{box-sizing:border-box;margin:0;padding:0}
html,body{width:1200px;height:3152px;overflow:hidden}
body{background:var(--white);font-family:'Open Sans',Arial,sans-serif;color:var(--text);position:relative}

/* header */
.site-header{height:64px;display:flex;align-items:center;padding:0 112px;justify-content:space-between}
.brand{font-family:'Montserrat',Arial,sans-serif;color:var(--ink);line-height:1}
.brand-top{font-size:17px;font-weight:700;letter-spacing:.5px}
.brand-bottom{font-size:15px;font-weight:500;letter-spacing:7px;margin-top:4px}
.main-nav{display:flex;gap:38px;font-family:'Montserrat',Arial,sans-serif;font-size:11px;font-weight:600;color:#444;margin-left:90px}
.main-nav a{color:inherit;text-decoration:none;padding-bottom:6px}
.main-nav a.active{color:var(--orange);border-bottom:2px solid var(--orange)}
.btn{display:inline-block;background:var(--orange);color:var(--white);font-family:'Montserrat',Arial,sans-serif;font-weight:600;font-size:12px;text-align:center;border-radius:4px;text-decoration:none}
.header-cta{width:160px;height:42px;line-height:42px;margin-left:auto}

/* hero */
.hero{position:relative;height:576px;overflow:hidden}
.hero-photo{position:absolute;inset:0;background:linear-gradient(100deg,#2a2624 0%,#4a403a 22%,#c9bfb4 45%,#a89a8c 60%,#5d5048 80%,#2d2724 100%)}
.hero-shade{position:absolute;inset:0;background:linear-gradient(90deg,rgba(0,0,0,0) 45%,rgba(0,0,0,.35) 100%)}
.hero-title{position:absolute;right:104px;top:116px;text-align:right;font-family:'Montserrat',Arial,sans-serif;font-weight:800;font-size:40px;line-height:1.15;letter-spacing:1.5px;color:var(--white)}
.hero-title .accent{color:var(--orange)}
.hero-arrow{position:absolute;top:320px;width:48px;height:48px;border:2px solid var(--white);border-radius:50%;display:flex;align-items:center;justify-content:center}
.hero-arrow.prev{left:40px}
.hero-arrow.next{right:40px}
.hero-dots{position:absolute;bottom:22px;left:50%;transform:translateX(-50%);display:flex;gap:8px}
.hero-dots span{width:8px;height:8px;border-radius:50%;background:rgba(255,255,255,.55)}
.hero-dots span.on{background:var(--orange)}

/* section titles */
.section-title{text-align:center;font-family:'Montserrat',Arial,sans-serif;font-size:38px;letter-spacing:3px;color:var(--ink);font-weight:500}
.section-title b{font-weight:800}

/* how we work */
.how{padding-top:66px;height:560px}
.service-cards{display:flex;gap:28px;justify-content:center;margin-top:46px}
.service-card{width:224px;height:190px;background:var(--white);border-radius:6px;box-shadow:0 4px 18px rgba(0,0,0,.12);text-align:center;padding:24px 20px 0}
.service-card svg{height:52px}
.service-card h3{font-family:'Montserrat',Arial,sans-serif;font-size:19px;font-weight:700;color:var(--orange);margin:12px 0 8px;letter-spacing:.5px}
.service-card p{font-size:11px;line-height:1.5;color:var(--muted)}
.how .btn{display:block;width:236px;height:46px;line-height:46px;margin:42px auto 0}

/* clients */
.clients{background:var(--band);height:480px;padding-top:106px}
.client-grid{display:grid;grid-template-columns:repeat(4,240px);width:960px;margin:48px auto 0}
.client{height:96px;display:flex;align-items:center;justify-content:center;gap:10px;font-family:'Montserrat',Arial,sans-serif;font-weight:700;font-size:22px;color:#2b2b2b;white-space:nowrap}
.client:not(:nth-child(4n)){border-right:1px solid #d2d2d2}
.client:nth-child(-n+4){border-bottom:1px solid #d2d2d2}
.client i{display:block;width:22px;height:22px;border-radius:50%;background:var(--orange);flex:none}

/* what we do */
.what{padding-top:118px;height:730px}
.post-cards{display:flex;gap:48px;justify-content:center;margin-top:30px}
.post-card{width:288px;height:380px;background:var(--white);box-shadow:0 4px 18px rgba(0,0,0,.12);border-radius:4px;overflow:hidden}
.post-photo{height:168px;background:linear-gradient(120deg,#d9c7b4 0%,#a88466 45%,#5f4a3c 100%)}
.post-body{padding:16px 16px 0}
.post-body h3{font-family:'Montserrat',Arial,sans-serif;font-size:13px;font-weight:700;color:var(--orange);line-height:1.45}
.post-body p{font-size:11px;line-height:1.6;color:var(--muted);margin-top:10px}
.post-tag{display:flex;align-items:center;gap:8px;margin-top:16px;font-family:'Montserrat',Arial,sans-serif;font-size:11px;font-weight:700;color:var(--ink)}
.what .btn{display:block;width:250px;height:46px;line-height:46px;margin:48px auto 0}

/* newsletter */
.newsletter{background:linear-gradient(90deg,var(--orange-deep),var(--orange));height:272px;padding:76px 112px 0;display:flex;justify-content:space-between}
.newsletter h2{font-family:'Montserrat',Arial,sans-serif;font-size:27px;font-weight:800;letter-spacing:1px;line-height:1.2;color:var(--white)}
.newsletter h2 .dark{color:var(--ink)}
.newsletter p{color:var(--white);font-size:19px;line-height:1.4;margin-top:12px}
.signup{width:392px;padding-top:8px}
.signup .field{height:40px;background:var(--white);border-radius:3px;padding:0 16px;line-height:40px;font-size:13px;color:#777}
.signup .btn{width:136px;height:40px;line-height:40px;margin-top:12px;background:var(--white);color:var(--ink)}

/* footer */
.site-footer{padding:72px 112px 0;display:flex;height:470px;position:relative}
.footer-brand{width:300px;padding-top:40px}
.socials{display:flex;gap:14px;margin-top:24px;padding-left:18px}
.socials span{width:36px;height:36px;border-radius:50%;background:var(--orange)}
.footer-col h4{font-family:'Montserrat',Arial,sans-serif;font-size:18px;font-weight:700;letter-spacing:1.5px;color:var(--ink);padding-bottom:10px;border-bottom:1px solid var(--line);margin-bottom:14px}
.footer-col ul{list-style:none;font-size:12px;line-height:2.1;color:#555}
.col-quick{width:180px;margin-left:10px}
.col-links{width:160px;margin-left:10px}
.col-service{width:250px;margin-left:20px}
.contact-line{display:flex;gap:14px;align-items:flex-start;font-size:11px;line-height:1.5;margin-bottom:16px}
.contact-line svg{flex:none}
.copyright{position:absolute;left:0;right:0;bottom:44px;text-align:center;font-size:11px;color:#777;border-top:1px solid var(--line);padding-top:20px;margin:0 112px}
.to-top{position:absolute;right:16px;bottom:100px;width:40px;height:40px;border-radius:50%;background:var(--orange);display:flex;align-items:center;justify-content:center}
</style>
</head>
<body>

<header class="site-header">
  <div class="brand"><div class="brand-top">LANTERNFIELD PROSE</div><div class="brand-bottom">STUDIO</div></div>
  <nav class="main-nav">
    <a class="active" href="#">HOME</a><a href="#">OUR WORK</a><a href="#">CAPABILITIES</a><a href="#">ABOUT US</a><a href="#">BLOG</a>
  </nav>
  <a class="btn header-cta" href="#">GET IN TOUCH</a>
</header>

<section class="hero">
  <div class="hero-photo" role="img" aria-label="Photo of hands signing a document at a wooden desk"></div>
  <div class="hero-shade"></div>
  <h1 class="hero-title">COMMUNICATE <span class="accent">YOUR</span><br><span class="accent">EXPERTISE</span> AND YOUR<br><span class="accent">CUSTOMER SUCESSES</span></h1>
  <div class="hero-arrow prev"><svg width="18" height="18" viewBox="0 0 18 18"><path d="M15 9H3M8 4L3 9l5 5" stroke="#fff" stroke-width="2" fill="none"/></svg></div>
  <div class="hero-arrow next"><svg width="18" height="18" viewBox="0 0 18 18"><path d="M3 9h12M10 4l5 5-5 5" stroke="#fff" stroke-width="2" fill="none"/></svg></div>
  <div class="hero-dots"><span></span><span class="on"></span><span></span></div>
</section>

<section class="how">
  <h2 class="section-title"><b>HOW</b> WE WORK</h2>
  <div class="service-cards">
    <article class="service-card">
      <svg viewBox="0 0 60 52" width="60"><g fill="none" stroke="#333" stroke-width="2.5"><circle cx="10" cy="10" r="6"/><circle cx="50" cy="42" r="6"/><path d="M16 10h26a8 8 0 0 1 0 16H18a8 8 0 0 0 0 16h26" stroke="#f26a21"/></g></svg>
      <h3>STRATEGY</h3>
      <p>We map audience, goals and message before a single word lands on the page.</p>
    </article>
    <article class="service-card">
      <svg viewBox="0 0 60 52" width="60"><g fill="none" stroke="#333" stroke-width="2.5"><rect x="18" y="4" width="38" height="26"/><path d="M24 22l8-8 6 5 10-9" stroke="#f26a21"/><circle cx="9" cy="14" r="5"/><path d="M2 48V28h14l10-6M16 28v20"/></g></svg>
      <h3>COACHING</h3>
      <p>We help your experts find their voice and write with calm, steady confidence.</p>
    </article>
    <article class="service-card">
      <svg viewBox="0 0 60 52" width="60"><g fill="none" stroke="#333" stroke-width="2.5"><path d="M8 6h32v40H8z"/><path d="M14 16h20M14 24h20M14 32h12"/><path d="M52 8l6 6-22 22-8 2 2-8z" stroke="#f26a21"/></g></svg>
      <h3>WRITING</h3>
      <p>Clear white papers, case studies and articles that turn technical depth into trust.</p>
    </article>
    <article class="service-card">
      <svg viewBox="0 0 60 52" width="60"><g fill="none" stroke="#333" stroke-width="2.5"><path d="M30 8H8v38h38V24"/><path d="M48 4l6 6-22 22-8 2 2-8z" stroke="#f26a21"/></g></svg>
      <h3>EDITING</h3>
      <p>We tighten structure, sharpen every sentence and keep your tone fully consistent.</p>
    </article>
  </div>
  <a class="btn" href="#">VIEW OUR CAPABILITIES</a>
</section>

<section class="clients">
  <h2 class="section-title"><b>OUR CLIENTS</b></h2>
  <div class="client-grid">
    <div class="client"><i></i>Norvale</div>
    <div class="client"><i></i>Quillon</div>
    <div class="client"><i></i>Brightmark</div>
    <div class="client"><i></i>Stackwise</div>
    <div class="client"><i></i>Pellham Ledger</div>
    <div class="client"><i></i>Tidewell</div>
    <div class="client"><i></i>Corvin</div>
    <div class="client"><i></i>Mossgate</div>
  </div>
</section>

<section class="what">
  <h2 class="section-title"><b>WHAT</b> WE DO</h2>
  <div class="post-cards">
    <article class="post-card">
      <div class="post-photo" role="img" aria-label="Photo of a person writing notes at a desk"></div>
      <div class="post-body">
        <h3>How to Align Your applications to the Optimal Infrastructure Environments</h3>
        <p>Practical guidance for teams planning a move to cloud platforms with less risk.</p>
        <div class="post-tag"><svg width="16" height="16" viewBox="0 0 16 16"><rect x="1" y="2" width="14" height="12" fill="none" stroke="#f26a21" stroke-width="2"/></svg>FIELD NOTES</div>
      </div>
    </article>
    <article class="post-card">
      <div class="post-photo" role="img" aria-label="Photo of hands writing on paper beside a laptop"></div>
      <div class="post-body">
        <h3>How to Align Your applications to the Optimal Infrastructure Environments</h3>
        <p>Practical guidance for teams planning a move to cloud platforms with less risk.</p>
        <div class="post-tag"><svg width="16" height="16" viewBox="0 0 16 16"><rect x="1" y="2" width="14" height="12" fill="none" stroke="#f26a21" stroke-width="2"/></svg>FIELD NOTES</div>
      </div>
    </article>
    <article class="post-card">
      <div class="post-photo" role="img" aria-label="Photo of a person writing in a notebook at a table"></div>
      <div class="post-body">
        <h3>How to Align Your applications to the Optimal Infrastructure Environments</h3>
        <p>Practical guidance for teams planning a move to cloud platforms with less risk.</p>
        <div class="post-tag"><svg width="16" height="16" viewBox="0 0 16 16"><rect x="1" y="2" width="14" height="12" fill="none" stroke="#f26a21" stroke-width="2"/></svg>FIELD NOTES</div>
      </div>
    </article>
  </div>
  <a class="btn" href="#">VIEW OUR WORK</a>
</section>

<section class="newsletter">
  <div>
    <h2>EDITORIAL INSPIRATION <span class="dark">DELIVERED</span><br>STRAIGHT TO YOUR INBOX.</h2>
    <p>Feel free to contact us with any questions.<br>We're happy to help.</p>
  </div>
  <div class="signup">
    <div class="field">Enter Your mail</div>
    <a class="btn" href="#">GET IN TOUCH</a>
  </div>
</section>

<footer class="site-footer">
  <div class="footer-brand">
    <div class="brand"><div class="brand-top">LANTERNFIELD PROSE</div><div class="brand-bottom">STUDIO</div></div>
    <div class="socials" aria-label="Social links"><span></span><span></span><span></span><span></span></div>
  </div>
  <div class="footer-col col-quick">
    <h4>QUICK LINKS</h4>
    <ul><li>Home</li><li>Our Work</li><li>Capabilities</li><li>About us</li><li>Blog</li></ul>
  </div>
  <div class="footer-col col-links">
    <h4>LINKS</h4>
    <ul><li>Copyright</li><li>Legal</li><li>Privacy</li><li>Accessibility</li><li>Sitemap</li></ul>
  </div>
  <div class="footer-col col-service">
    <h4>CUSTOMER SERVICE</h4>
    <div class="contact-line"><svg width="14" height="18" viewBox="0 0 14 18"><path d="M7 1a6 6 0 0 1 6 6c0 4-6 10-6 10S1 11 1 7a6 6 0 0 1 6-6z" fill="#f26a21"/><circle cx="7" cy="7" r="2" fill="#fff"/></svg><span>1420 Alder Lane, Harbor Bend,<br>Oregon, USA</span></div>
    <div class="contact-line"><svg width="14" height="14" viewBox="0 0 14 14"><path d="M3 1l3 3-2 2a8 8 0 0 0 4 4l2-2 3 3-2 2C6 13 1 8 1 3z" fill="#f26a21"/></svg><span>555 014 2288</span></div>
    <div class="contact-line"><svg width="16" height="12" viewBox="0 0 16 12"><rect x="1" y="1" width="14" height="10" fill="none" stroke="#f26a21" stroke-width="2"/><path d="M1 1l7 6 7-6" fill="none" stroke="#f26a21" stroke-width="2"/></svg><span>hello@lpstudio.net</span></div>
  </div>
  <div class="to-top"><svg width="14" height="14" viewBox="0 0 14 14"><path d="M2 9l5-5 5 5" stroke="#fff" stroke-width="2" fill="none"/></svg></div>
  <div class="copyright">© 2021 . ALL RIGHTS RESERVED</div>
</footer>

</body>
</html>
```